Love for my Family

It´s pobably a straight forward and boring request, but I´d love to get the names of my wife and my children including their birthdays to express that they are the most important things in my life and will stay with me forever.
As I have not tattoo today I´d rather have an timeless design that makrs up for itseld as single tattoo in a subtile way.
I hope this helps.
Here are the names dates if this helps:
Helene Brunsack - 25.05.1982
Lorenz Brunsack - 28.01.2019
Matthias Brunsack - 06.06.2021

```html
<!DOCTYPE html>
<html lang="de">
<head>
<meta charset="utf-8">
<title>Love for my Family – Brunsack</title>
<link rel="stylesheet" href="https://fonts.googleapis.com/css2?family=Cinzel:wght@400;500&display=swap">
<style>
  :root {
    --ink: #000000;
    --paper: #ffffff;
  }
  html, body {
    margin: 0;
    padding: 0;
    overflow: hidden;
    background: var(--paper);
  }
  .canvas {
    position: relative;
    width: 1200px;
    height: 1093px;
    overflow: hidden;
    background: var(--paper);
    color: var(--ink);
    font-family: "Cinzel", serif;
  }
  .entry {
    position: absolute;
    text-align: center;
    line-height: 1;
  }
  .entry .name {
    display: block;
    border-bottom: 4px solid var(--ink);
    white-space: nowrap;
  }
  .entry .date {
    display: block;
    white-space: nowrap;
  }

  /* Variant A: three columns */
  .variant-a .entry .name { font-size: 62px; padding-bottom: 2px; }
  .variant-a .entry .date { font-size: 70px; margin-top: 8px; }
  .variant-a .entry { top: 14px; }

  /* Variant B: columns with surname */
  .variant-b .entry .name { font-size: 48px; padding-bottom: 1px; border-bottom-width: 3px; }
  .variant-b .entry .date { font-size: 54px; margin-top: 6px; }
  .variant-b .entry { top: 362px; }
  .family-rule {
    position: absolute;
    left: 3px;
    top: 506px;
    width: 946px;
    height: 6px;
    background: var(--ink);
  }
  .surname {
    position: absolute;
    left: 0;
    width: 952px;
    top: 518px;
    text-align: center;
    font-size: 158px;
    line-height: 1;
    margin: 0;
    font-weight: 400;
  }

  /* Variant C: single lines */
  .line-list {
    position: absolute;
    left: 3px;
    top: 808px;
    margin: 0;
    padding: 0;
    list-style: none;
    font-size: 56px;
    line-height: 83px;
    white-space: nowrap;
  }
</style>
</head>
<body>
<main class="canvas">

  <section class="variant-a">
    <div class="entry" style="left:6px;width:336px;">
      <span class="name">Helene</span>
      <span class="date">25.05.1982</span>
    </div>
    <div class="entry" style="left:384px;width:360px;">
      <span class="name">Lorenz</span>
      <span class="date">28.01.2019</span>
    </div>
    <div class="entry" style="left:780px;width:380px;">
      <span class="name">Matthias</span>
      <span class="date">06.06.2021</span>
    </div>
  </section>

  <section class="variant-b">
    <div class="entry" style="left:6px;width:270px;">
      <span class="name">Helene</span>
      <span class="date">25.05.1982</span>
    </div>
    <div class="entry" style="left:316px;width:294px;">
      <span class="name">Lorenz</span>
      <span class="date">28.01.2019</span>
    </div>
    <div class="entry" style="left:640px;width:314px;">
      <span class="name">Matthias</span>
      <span class="date">06.06.2021</span>
    </div>
    <div class="family-rule"></div>
    <h1 class="surname">Brunsack</h1>
  </section>

  <ul class="line-list">
    <li>Helene Brunsack - 25.05.1982</li>
    <li>Lorenz Brunsack - 28.01.2019</li>
    <li>Matthias Brunsack - 06.06.2021</li>
  </ul>

</main>
</body>
</html>
```